Broschüre KTR Festival
Zielgruppe
Wir sind ein Verband, der Ensembles der Amateurmusik (Blasorchester, Chöre, Akkordeonensembles ....) vertritt. Unsere Zielgruppe sind Menschen, die in ihrer Freizeit musizieren ebenso, wie Menschen die gerne Konzerte besuchen.
Die Broschüre ist ein Programmheft für ein eintägiges Festival mit mehreren Open-Air Bühnen.
Aufgabenstellung
Die Broschüre sollte DIN lang Format sein, damit sie gut in die Westentasche passt. Zentraler Bestandteil neben den Textseiten sind die Termintabellen, die die Auftritte auf den Bühnen abbilden.

```html
<!DOCTYPE html>
<html lang="de">
<head>
<meta charset="utf-8">
<title>KTR Festival – Programmheft</title>
<link rel="stylesheet" href="https://fonts.googleapis.com/css2?family=Montserrat:wght@300;400;600;700;800&display=swap">
<style>
:root{
  --teal:#2aa394;
  --teal-dark:#1f8a7d;
  --teal-light:#8fe3d6;
  --paper:#e9ebea;
  --ink:#4a4a4a;
  --white:#ffffff;
  --bg:#c9c9c9;
  --stripe-red:#e0433a;
  --stripe-orange:#f2a23a;
  --stripe-blue:#3b62b8;
  --smoke:#7d7068;
}
*{margin:0;padding:0;box-sizing:border-box}
html,body{width:1200px;height:750px;overflow:hidden}
body{background:var(--bg);font-family:"Montserrat",sans-serif;display:flex;align-items:center;justify-content:center}
.brochure{display:flex;gap:14px}
.panel{width:330px;height:690px;position:relative;overflow:hidden;background:var(--teal)}
.stripes{position:absolute;left:0;right:0;height:7px;background:linear-gradient(var(--stripe-blue) 0 33%,var(--stripe-orange) 33% 66%,var(--stripe-red) 66% 100%)}
.stripes.top{top:0}
.stripes.bottom{bottom:0}
.web{position:absolute;bottom:14px;left:0;right:0;text-align:center;font-size:9px;letter-spacing:2px;color:rgba(255,255,255,.75)}

/* cover */
.cover-image{position:absolute;top:7px;left:0;right:0;height:420px;background:radial-gradient(circle at 55% 55%,var(--smoke) 0 35%,#a59a92 55%,#e8e4df 80%)}
.cover-title{position:absolute;top:190px;left:70px;transform:rotate(-25deg);transform-origin:left top;color:var(--white);font-weight:700;display:flex;gap:10px;align-items:flex-start}
.cover-title .mark{width:14px;height:14px;background:var(--white);margin-top:8px}
.cover-title .name{font-size:38px;line-height:1}
.cover-title .date{font-size:22px;line-height:1.15;margin-top:8px;font-weight:700}
.claim{position:absolute;bottom:110px;left:40px;transform:rotate(-25deg);color:var(--white);font-weight:800;font-size:36px;line-height:1.05;text-align:center}

/* schedule */
.schedule{padding:30px 26px 0}
.slot{position:relative;padding:14px 0 12px;border-bottom:1px dotted rgba(255,255,255,.5)}
.slot .time{position:absolute;right:0;top:6px;font-size:40px;font-weight:300;color:rgba(255,255,255,.28)}
.slot .title{font-size:17px;font-weight:700;color:var(--white)}
.slot .theme{font-size:10px;font-weight:600;color:var(--teal-light);letter-spacing:.5px;margin-top:3px}
.slot .place{font-size:9px;color:rgba(255,255,255,.7);letter-spacing:.5px}
.info{padding:26px 26px 0;color:var(--white)}
.info h2{font-size:21px;font-weight:700;margin-bottom:8px}
.info p{font-size:13px;font-weight:600;line-height:1.4}
.ghost-name{position:absolute;right:-40px;top:300px;transform:rotate(-90deg);font-size:44px;font-weight:800;color:rgba(255,255,255,.12)}

/* artists */
.artists{background:var(--paper);padding:24px 20px 0}
.photo{height:170px;background:linear-gradient(160deg,#c9cfd0,#7c8a8e)}
.photo.band{background:linear-gradient(160deg,#b7c4cc,#5b6770)}
.artist{padding:12px 4px 18px;text-align:right}
.artist h3{font-size:16px;font-weight:700;color:var(--teal)}
.artist .meta{font-size:8.5px;font-weight:600;color:var(--teal-dark);margin:2px 0 6px}
.artist p{font-size:9.5px;line-height:1.5;color:var(--ink)}
.artists .web{color:var(--teal)}
</style>
</head>
<body>
<main class="brochure">
  <section class="panel cover">
    <div class="stripes top"></div>
    <div class="cover-image" role="img" aria-label="Collage aus Harfe, Trompete, Flügel, Geige und Cello in brauner Rauchwolke"></div>
    <div class="cover-title">
      <span class="mark"></span>
      <div>
        <div class="name">KTR Festival</div>
        <div class="date">11.07.2020<br>Überlingen</div>
      </div>
    </div>
    <div class="claim">NATÜRLICH<br>MUSIK!</div>
    <div class="stripes bottom"></div>
  </section>

  <section class="panel program">
    <div class="stripes top"></div>
    <div class="ghost-name">KTR Festival</div>
    <div class="schedule">
      <div class="slot"><span class="time">13:30</span><div class="title">Eventi Title</div><div class="theme">CONCERT THEME NUMBER 4</div><div class="place">LOCATION GOES HERE</div></div>
      <div class="slot"><span class="time">14:30</span><div class="title">Eventi Title</div><div class="theme">CONCERT THEME NUMBER 5</div><div class="place">LOCATION GOES HERE</div></div>
      <div class="slot"><span class="time">16:30</span><div class="title">Eventi Title</div><div class="theme">CONCERT THEME NUMBER 6</div><div class="place">LOCATION GOES HERE</div></div>
      <div class="slot"><span class="time">19:30</span><div class="title">Eventi Title</div><div class="theme">CONCERT THEME NUMBER 7</div><div class="place">LOCATION GOES HERE</div></div>
      <div class="slot"><span class="time">22:30</span><div class="title">Eventi Title</div><div class="theme">CONCERT THEME NUMBER 8</div><div class="place">LOCATION GOES HERE</div></div>
    </div>
    <div class="info">
      <h2>Info and Tickets</h2>
      <p>+49 00 98 76 54 321<br>tickets@ktr-fest-beispiel.de</p>
    </div>
    <div class="web">www.ktr-fest-beispiel.de</div>
    <div class="stripes bottom"></div>
  </section>

  <section class="panel artists">
    <div class="stripes top"></div>
    <div class="photo" role="img" aria-label="Chor auf einer Open-Air-Bühne mit Dirigent"></div>
    <div class="artist">
      <h3>Artist or Band Name</h3>
      <div class="meta">TITLE OF THE THEME - MUSIC START H 10.00</div>
      <p>Ein Chor aus der Region singt Lieder unter freiem Himmel, mit viel Freude, Klang und Herz für das ganze Publikum am See.</p>
    </div>
    <div class="photo band" role="img" aria-label="Blasorchester beim Spielen im Freien"></div>
    <div class="artist">
      <h3>Artist or Band Name</h3>
      <div class="meta">TITLE OF THE THEME - MUSIC START H 10.00</div>
      <p>Das Blasorchester spielt bekannte Stücke und neue Werke, frisch geprobt für einen Sommerabend voller Musik im Freien.</p>
    </div>
    <div class="web">www.ktr-fest-beispiel.de</div>
    <div class="stripes bottom"></div>
  </section>
</main>
</body>
</html>
```